Covid19 Poster for workplaces

Create a poster on how to protect yourself from Corona virus at work.
We are a workplace wellbeing company. We have just re-branded so we need to fit in with our brand. We like clean and fresh, slightly amusing is ok if it will draw attention but it's an important topic. A4 and A3 please.

Content:

Headline: Lower the risk of COVID 19 in the workplace.

BE WELL

Bring your own cup - don’t share cups and food.
Elbow tap instead of handshakes and kisses
Wash your hands often - with soap.
Elbow or tissues when you cough or sneeze then straight in the bin
Leave your face alone after touching shared surfaces
Leave your bugs at home if you’re feeling unwell.

Call health line if you have a cough, a high temperature and shortness of breath. 0800 472 9160

Based on recommendations from ZPK and QLN

Target Market(s)

Employees - so anyone

Other font styles liked:
• Use the closest font to the brand documents

Requirements
Should not have
• Clip art

```html
<!DOCTYPE html>
<html lang="en">
<head>
<meta charset="utf-8">
<title>Lower the risk of COVID-19 in the workplace – poster variants</title>
<link rel="stylesheet" href="https://fonts.googleapis.com/css2?family=Montserrat:wght@200;700;800&family=Quicksand:wght@500;600&display=swap">
<style>
  :root {
    --navy: #2d3592;
    --blue-start: #2e3797;
    --blue-end: #2778c8;
    --ink: #000000;
    --paper: #ffffff;
    --sun: #ffd400;
    --lavender: #8f95cf;
    --overlay: rgba(70, 80, 175, 0.62);
    --heading: "Montserrat", sans-serif;
    --body: "Quicksand", sans-serif;
  }
  * { box-sizing: border-box; margin: 0; padding: 0; }
  html, body { width: 881px; height: 1200px; overflow: hidden; background: var(--paper); }
  .board { position: relative; width: 881px; height: 1200px; }

  .poster {
    position: absolute; width: 372px; height: 525px; overflow: hidden;
    box-shadow: 0 4px 22px rgba(0,0,0,0.18);
    color: var(--paper);
  }
  .poster--tl { left: 52px; top: 46px; }
  .poster--tr { left: 457px; top: 46px; }
  .poster--bl { left: 52px; top: 619px; }
  .poster--br { left: 457px; top: 619px; }

  .poster--blue { background: linear-gradient(150deg, var(--blue-start) 0%, var(--blue-start) 25%, var(--blue-end) 100%); }
  .poster--black { background: var(--ink); }
  .poster--white, .poster--white-alt { background: var(--paper); color: var(--ink); }

  .virus-art {
    position: absolute; left: -30px; top: -28px; width: 150px; height: 170px;
    border-radius: 48% 48% 10% 48%;
    transform: rotate(45deg) scale(0.82);
    background: radial-gradient(circle at 40% 45%, #5d6c73 0%, #3a4a58 45%, #6b6f98 100%);
    opacity: 0.9;
  }
  .poster--black .virus-art { background: radial-gradient(circle at 40% 45%, #6b6a3a 0%, #3c4020 50%, #4f5a62 100%); }
  .poster--white .virus-art, .poster--white-alt .virus-art {
    background: radial-gradient(circle at 40% 45%, #ecebb8 0%, #d9dca6 45%, #bfe0e8 100%);
  }

  .line { display: block; white-space: nowrap; }
  .line--spread { text-align: justify; text-align-last: justify; }

  .headline {
    position: absolute; left: 88px; top: 28px; width: 262px;
    font-family: var(--heading); font-weight: 800; font-size: 19.5px;
    line-height: 23px; letter-spacing: 0.06em; text-transform: uppercase;
  }
  .poster--white-alt .headline { left: 92px; top: 25px; width: 226px; font-size: 19px; line-height: 20.5px; }
  .headline-rule { position: absolute; left: 94px; top: 97px; width: 11px; height: 3px; background: var(--navy); }

  .tips { position: absolute; left: 74px; top: 117px; width: 276px; list-style: none; }
  .tip {
    position: relative; padding-left: 16px; margin-bottom: 10px;
    font-family: var(--body); font-weight: 500; font-size: 11.7px; line-height: 12.4px; letter-spacing: 0.03em;
  }
  .tip svg { position: absolute; left: 0; top: 3px; width: 11px; height: 8px; }

  .word-corona, .word-virus {
    position: absolute; writing-mode: vertical-rl; transform: rotate(180deg);
    font-family: var(--heading); text-transform: uppercase; line-height: 1; color: var(--navy);
  }
  .word-corona { left: 0; bottom: 12px; font-size: 69px; font-weight: 800; letter-spacing: -0.02em; }
  .word-virus { left: 40px; bottom: 21px; font-size: 63px; font-weight: 200; letter-spacing: 0.01em; }
  .poster--blue .word-corona { color: var(--lavender); }
  .poster--blue .word-virus { color: var(--paper); }

  .photo {
    position: absolute; left: 248px; top: 360px; width: 124px; height: 165px;
    border-radius: 62px 0 0 0 / 70px 0 0 0;
    background: linear-gradient(180deg, #8a6a55 0%, #c9a790 35%, #dfe4ea 60%, #d7a24a 100%);
  }
  .poster--white .photo, .poster--white-alt .photo {
    left: 215px; top: 360px; width: 157px; height: 165px; border-radius: 0;
    background: linear-gradient(90deg, rgba(255,255,255,1) 0%, rgba(230,220,212,0.6) 35%, #c9a790 65%, #d8a956 100%);
  }

  .helpline {
    position: absolute; left: 107px; top: 316px; width: 122px;
    font-family: var(--heading); font-weight: 700; font-size: 8.8px; line-height: 15.5px;
    letter-spacing: 0.08em; text-transform: uppercase;
  }
  .poster--black .helpline, .poster--white .helpline { left: 115px; width: 131px; }
  .poster--white-alt .helpline { left: 118px; top: 320px; width: 126px; line-height: 13.9px; }

  .phone {
    position: absolute; left: 105px; top: 395px; width: 150px;
    font-family: var(--heading); font-weight: 800; font-size: 24.5px; line-height: 25px;
    letter-spacing: 0.04em; color: var(--sun);
  }
  .poster--black .phone { left: 114px; }
  .poster--white .phone { left: 113px; top: 396px; }
  .poster--white-alt .phone { left: 116px; top: 391px; }

  .source {
    position: absolute; left: 105px; top: 455px; width: 130px;
    font-family: var(--body); font-weight: 500; font-size: 11px; line-height: 13.6px; letter-spacing: 0.03em;
  }
  .poster--black .source { left: 114px; }
  .poster--white .source { left: 114px; top: 460px; }
  .poster--white-alt .source {
    left: 109px; top: 448px; width: 263px; height: 58px; padding: 5px 0 0 7px;
    background: var(--overlay); color: var(--paper);
  }
</style>
</head>
<body>
<main class="board">

  <!-- Blue variant -->
  <article class="poster poster--tl poster--blue">
    <div class="virus-art" role="img" aria-label="Microscopic virus particles in a heart-shaped frame"></div>
    <h1 class="headline"><span class="line">Lower the risk of</span><span class="line">COVID-19 in the</span><span class="line">workplace</span></h1>
    <ul class="tips">
      <li class="tip"><svg viewBox="0 0 11 8"><path d="M5.5 8 0.6 3.4A2 2 0 0 1 5.5 1a2 2 0 0 1 4.9 2.4Z" fill="#ffd400"/></svg>Bring your own cup – don’t share cups and food</li>
      <li class="tip"><svg viewBox="0 0 11 8"><path d="M5.5 8 0.6 3.4A2 2 0 0 1 5.5 1a2 2 0 0 1 4.9 2.4Z" fill="#ffd400"/></svg>Elbow tap instead of handshakes and kisses</li>
      <li class="tip"><svg viewBox="0 0 11 8"><path d="M5.5 8 0.6 3.4A2 2 0 0 1 5.5 1a2 2 0 0 1 4.9 2.4Z" fill="#ffd400"/></svg>Wash your hands often – with soap</li>
      <li class="tip"><svg viewBox="0 0 11 8"><path d="M5.5 8 0.6 3.4A2 2 0 0 1 5.5 1a2 2 0 0 1 4.9 2.4Z" fill="#ffd400"/></svg>Elbow or tissues when you cough or sneeze then straight in the bin</li>
      <li class="tip"><svg viewBox="0 0 11 8"><path d="M5.5 8 0.6 3.4A2 2 0 0 1 5.5 1a2 2 0 0 1 4.9 2.4Z" fill="#ffd400"/></svg>Leave your face alone after touching shared surfaces</li>
      <li class="tip"><svg viewBox="0 0 11 8"><path d="M5.5 8 0.6 3.4A2 2 0 0 1 5.5 1a2 2 0 0 1 4.9 2.4Z" fill="#ffd400"/></svg>Leave your bugs at home if you’re feeling unwell</li>
    </ul>
    <span class="word-corona">Corona</span>
    <span class="word-virus">Virus</span>
    <div class="photo" role="img" aria-label="Photo of a woman wearing a surgical face mask"></div>
    <p class="helpline"><span class="line line--spread">Call health line if</span><span class="line line--spread">you have a cough, a</span><span class="line line--spread">high temperature</span><span class="line line--spread">and shortness of</span><span class="line">breath</span></p>
    <p class="phone">0800 472<br>9160</p>
    <p class="source">Based on<br>recommendations<br>from ZPK and QLN</p>
  </article>

  <!-- Black variant -->
  <article class="poster poster--tr poster--black">
    <div class="virus-art" role="img" aria-label="Microscopic virus particles in a heart-shaped frame"></div>
    <h1 class="headline"><span class="line">Lower the risk of</span><span class="line">COVID-19 in the</span><span class="line">workplace</span></h1>
    <ul class="tips">
      <li class="tip"><svg viewBox="0 0 11 8"><path d="M5.5 8 0.6 3.4A2 2 0 0 1 5.5 1a2 2 0 0 1 4.9 2.4Z" fill="#ffd400"/></svg>Bring your own cup – don’t share cups and food</li>
      <li class="tip"><svg viewBox="0 0 11 8"><path d="M5.5 8 0.6 3.4A2 2 0 0 1 5.5 1a2 2 0 0 1 4.9 2.4Z" fill="#ffd400"/></svg>Elbow tap instead of handshakes and kisses</li>
      <li class="tip"><svg viewBox="0 0 11 8"><path d="M5.5 8 0.6 3.4A2 2 0 0 1 5.5 1a2 2 0 0 1 4.9 2.4Z" fill="#ffd400"/></svg>Wash your hands often – with soap</li>
      <li class="tip"><svg viewBox="0 0 11 8"><path d="M5.5 8 0.6 3.4A2 2 0 0 1 5.5 1a2 2 0 0 1 4.9 2.4Z" fill="#ffd400"/></svg>Elbow or tissues when you cough or sneeze then straight in the bin</li>
      <li class="tip"><svg viewBox="0 0 11 8"><path d="M5.5 8 0.6 3.4A2 2 0 0 1 5.5 1a2 2 0 0 1 4.9 2.4Z" fill="#ffd400"/></svg>Leave your face alone after touching shared surfaces</li>
      <li class="tip"><svg viewBox="0 0 11 8"><path d="M5.5 8 0.6 3.4A2 2 0 0 1 5.5 1a2 2 0 0 1 4.9 2.4Z" fill="#ffd400"/></svg>Leave your bugs at home if you’re feeling unwell</li>
    </ul>
    <span class="word-corona">Corona</span>
    <span class="word-virus">Virus</span>
    <div class="photo" role="img" aria-label="Photo of a woman wearing a surgical face mask"></div>
    <p class="helpline"><span class="line line--spread">Call health line if</span><span class="line line--spread">you have a cough,</span><span class="line line--spread">a high temperature</span><span class="line line--spread">and shortness of</span><span class="line">breath</span></p>
    <p class="phone">0800 472<br>9160</p>
    <p class="source">Based on<br>recommendations<br>from ZPK and QLN</p>
  </article>

  <!-- White variant -->
  <article class="poster poster--bl poster--white">
    <div class="virus-art" role="img" aria-label="Pale yellow virus particles in a heart-shaped frame"></div>
    <h1 class="headline"><span class="line">Lower the risk of</span><span class="line">COVID-19 in the</span><span class="line">workplace</span></h1>
    <ul class="tips">
      <li class="tip"><svg viewBox="0 0 11 8"><path d="M5.5 8 0.6 3.4A2 2 0 0 1 5.5 1a2 2 0 0 1 4.9 2.4Z" fill="#ffd400"/></svg>Bring your own cup – don’t share cups and food</li>
      <li class="tip"><svg viewBox="0 0 11 8"><path d="M5.5 8 0.6 3.4A2 2 0 0 1 5.5 1a2 2 0 0 1 4.9 2.4Z" fill="#ffd400"/></svg>Elbow tap instead of handshakes and kisses</li>
      <li class="tip"><svg viewBox="0 0 11 8"><path d="M5.5 8 0.6 3.4A2 2 0 0 1 5.5 1a2 2 0 0 1 4.9 2.4Z" fill="#ffd400"/></svg>Wash your hands often – with soap</li>
      <li class="tip"><svg viewBox="0 0 11 8"><path d="M5.5 8 0.6 3.4A2 2 0 0 1 5.5 1a2 2 0 0 1 4.9 2.4Z" fill="#ffd400"/></svg>Elbow or tissues when you cough or sneeze then straight in the bin</li>
      <li class="tip"><svg viewBox="0 0 11 8"><path d="M5.5 8 0.6 3.4A2 2 0 0 1 5.5 1a2 2 0 0 1 4.9 2.4Z" fill="#ffd400"/></svg>Leave your face alone after touching shared surfaces</li>
      <li class="tip"><svg viewBox="0 0 11 8"><path d="M5.5 8 0.6 3.4A2 2 0 0 1 5.5 1a2 2 0 0 1 4.9 2.4Z" fill="#ffd400"/></svg>Leave your bugs at home if you’re feeling unwell</li>
    </ul>
    <span class="word-corona">Corona</span>
    <span class="word-virus">Virus</span>
    <div class="photo" role="img" aria-label="Photo of a woman wearing a surgical face mask, fading into white"></div>
    <p class="helpline"><span class="line line--spread">Call health line if</span><span class="line line--spread">you have a cough,</span><span class="line line--spread">a high temperature</span><span class="line line--spread">and shortness of</span><span class="line">breath</span></p>
    <p class="phone">0800 472<br>9160</p>
    <p class="source">Based on<br>recommendations<br>from ZPK and QLN</p>
  </article>

  <!-- White variant with source panel -->
  <article class="poster poster--br poster--white-alt">
    <div class="virus-art" role="img" aria-label="Pale yellow virus particles in a heart-shaped frame"></div>
    <h1 class="headline"><span class="line">Lower the risk of</span><span class="line line--spread">COVID-19 in the</span><span class="line">workplace</span></h1>
    <span class="headline-rule"></span>
    <ul class="tips">
      <li class="tip"><svg viewBox="0 0 11 8"><path d="M5.5 8 0.6 3.4A2 2 0 0 1 5.5 1a2 2 0 0 1 4.9 2.4Z" fill="#ffd400"/></svg>Bring your own cup – don’t share cups and food</li>
      <li class="tip"><svg viewBox="0 0 11 8"><path d="M5.5 8 0.6 3.4A2 2 0 0 1 5.5 1a2 2 0 0 1 4.9 2.4Z" fill="#ffd400"/></svg>Elbow tap instead of handshakes and kisses</li>
      <li class="tip"><svg viewBox="0 0 11 8"><path d="M5.5 8 0.6 3.4A2 2 0 0 1 5.5 1a2 2 0 0 1 4.9 2.4Z" fill="#ffd400"/></svg>Wash your hands often – with soap</li>
      <li class="tip"><svg viewBox="0 0 11 8"><path d="M5.5 8 0.6 3.4A2 2 0 0 1 5.5 1a2 2 0 0 1 4.9 2.4Z" fill="#ffd400"/></svg>Elbow or tissues when you cough or sneeze then straight in the bin</li>
      <li class="tip"><svg viewBox="0 0 11 8"><path d="M5.5 8 0.6 3.4A2 2 0 0 1 5.5 1a2 2 0 0 1 4.9 2.4Z" fill="#ffd400"/></svg>Leave your face alone after touching shared surfaces</li>
      <li class="tip"><svg viewBox="0 0 11 8"><path d="M5.5 8 0.6 3.4A2 2 0 0 1 5.5 1a2 2 0 0 1 4.9 2.4Z" fill="#ffd400"/></svg>Leave your bugs at home if you’re feeling unwell</li>
    </ul>
    <span class="word-corona">Corona</span>
    <span class="word-virus">Virus</span>
    <div class="photo" role="img" aria-label="Photo of a woman wearing a surgical face mask, fading into white"></div>
    <p class="helpline"><span class="line line--spread">Call health line if</span><span class="line line--spread">you have a cough, a</span><span class="line line--spread">high temperature</span><span class="line line--spread">and shortness of</span><span class="line">breath</span></p>
    <p class="phone">0800 472<br>9160</p>
    <p class="source">Based on<br>recommendations<br>from ZPK and QLN</p>
  </article>

</main>
</body>
</html>
```